Business Card Design Project

I need a business card design for an Organic drive thru coffee kiosk. We will serve organic coffee, teas & smoothies and will serve healthy breakfast food/snacks for people on the go.
I want the card to have 2-3 colors max (earthy colors like browns, greens and so on).
I have attached the logo I want used and would love to play off the theme of "balance."
Include:
Tidy-Kettle Coffee
address: 4820 Gorvin Ct. Raleigh, NC 27583
phone: 919-731-4062
website: www.tidy-kettle.com (website is not up yet but still include it on card)
email: Rosalind@tidy-kettle.com
I want one of the following sayings somewhere on the card (the front or back is fine):
"Eat & Drink Well, on the run!"
"Break the fast with Tidy-Kettle"
Maybe on the back list what we offer:
-Organic coffee, espresso & tea
-Blendora smoothies & protein shakes
-Zesty Pour (100% fresh local fruit and veggies)
-Tender Nibs

```html
<!DOCTYPE html>
<html lang="en">
<head>
<meta charset="utf-8">
<title>Tidy-Kettle Coffee — Business Cards</title>
<link rel="stylesheet" href="https://fonts.googleapis.com/css2?family=Josefin+Sans:wght@400&family=Open+Sans:ital,wght@0,400;0,600;0,700;1,600;1,700&family=Dancing+Script:wght@600&display=swap">
<style>
  :root {
    --page: #ffffff;
    --ink: #4a2c1e;
    --ink-soft: #6b3f22;
    --peach: #fdd3a8;
    --apricot: #fbb068;
    --orange: #d9701a;
    --roast: #83410f;
    --sun: #f2c53c;
    --cream: #fdf6da;
    --blush: #f9d2ac;
    --tan: #e3ba8e;
    --sand: #ecd6bf;
    --divider: #ffffff;
    --label: #3a2414;
    --wordmark: "Josefin Sans", sans-serif;
    --body: "Open Sans", sans-serif;
    --script: "Dancing Script", cursive;
  }
  * { box-sizing: border-box; margin: 0; padding: 0; }
  html, body { width: 1200px; height: 900px; overflow: hidden; background: var(--page); }
  .canvas { position: relative; width: 1200px; height: 900px; }

  .card {
    position: absolute; left: 240px; width: 720px; height: 411px;
    overflow: hidden; box-shadow: 0 4px 14px rgba(0,0,0,.25);
    font-family: var(--body);
  }
  .card--front { top: 26px; background: var(--peach); }
  .card--back { top: 463px; background: var(--cream); }

  .band { position: absolute; top: 0; bottom: 0; border-left: 3px solid var(--divider); }
  .card--front .band--light { left: 373px; width: 87px; background: var(--apricot); }
  .card--front .band--mid { left: 460px; width: 107px; background: var(--orange); }
  .card--front .band--dark { left: 567px; width: 153px; background: var(--roast); }
  .card--back .band { border-left-color: rgba(255,255,255,.7); }
  .card--back .band--light { left: 400px; width: 95px; background: var(--blush); }
  .card--back .band--mid { left: 495px; width: 115px; background: var(--tan); }
  .card--back .band--dark { left: 610px; width: 110px; background: var(--sand); }

  .brand-name {
    position: absolute; left: 0; width: 373px; top: 22px; text-align: center;
    font-family: var(--wordmark); font-weight: 400; font-size: 64px; color: var(--ink);
    line-height: 1;
  }
  .brand-disc { position: absolute; left: 130px; top: 140px; width: 110px; height: 110px; }

  .saying { position: absolute; font-family: var(--script); font-weight: 600; white-space: nowrap; }
  .card--front .saying--break { left: 252px; top: 262px; font-size: 20px; color: #5a2e10; }
  .card--front .saying--run { left: 472px; top: 176px; font-size: 19px; color: #fff4e4; }
  .card--back .saying--break { left: 200px; top: 82px; font-size: 19px; color: #7a3e14; }
  .card--back .saying--run { left: 408px; top: 24px; font-size: 18px; color: #8a5a36; }

  .contact { position: absolute; font-size: 12.5px; font-weight: 600; color: var(--label); line-height: 1.85; white-space: nowrap; }
  .contact b { font-size: 9.5px; font-weight: 700; letter-spacing: .3px; }
  .card--front .contact--place { left: 18px; top: 346px; }
  .card--front .contact--web { left: 472px; top: 346px; color: #2b1608; }
  .card--back .contact--web { left: 408px; top: 344px; color: #6b4a33; }

  .menu { position: absolute; left: 128px; top: 140px; color: var(--label); }
  .menu__title { font-size: 20px; font-weight: 700; padding-bottom: 6px; border-bottom: 2px solid #b8c7d4; width: 240px; margin-bottom: 14px; }
  .menu__list { list-style: none; font-size: 13px; font-weight: 700; font-style: italic; }
  .menu__list li { margin-bottom: 13px; }
  .menu__list li::before { content: "~ "; }
  .menu__note { display: block; font-size: 9px; font-weight: 600; padding-left: 18px; margin-top: 1px; }

  .vertical-name {
    position: absolute; left: 724px; top: 12px; transform-origin: 0 0; transform: rotate(90deg);
    font-family: var(--wordmark); font-size: 66px; color: rgba(140,95,60,.35); white-space: nowrap; line-height: 1;
  }
</style>
</head>
<body>
<main class="canvas">
  <section class="card card--front" aria-label="Card front">
    <div class="band band--light"></div>
    <div class="band band--mid"></div>
    <div class="band band--dark"></div>
    <h1 class="brand-name">Tidy-Kettle</h1>
    <svg class="brand-disc" viewBox="0 0 110 110" aria-hidden="true"><circle cx="55" cy="55" r="55" fill="var(--sun)"/></svg>
    <p class="saying saying--break">Break the fast with Tidy-Kettle</p>
    <p class="saying saying--run">Eat &amp; Drink Well, on the run</p>
    <p class="contact contact--place"><b>ADDRESS:</b> 4820 Gorvin Ct. Raleigh, NC 27583<br><b>PHONE:</b> 919-731-4062</p>
    <p class="contact contact--web"><b>WEBSITE:</b> www.tidy-kettle.com<br><b>EMAIL:</b> Rosalind@tidy-kettle.com</p>
  </section>

  <section class="card card--back" aria-label="Card back">
    <div class="band band--light"></div>
    <div class="band band--mid"></div>
    <div class="band band--dark"></div>
    <p class="vertical-name">Tidy-Kettle</p>
    <p class="saying saying--run">Eat &amp; Drink Well, On The Run</p>
    <p class="saying saying--break">Break The Fast With Tidy-Kettle</p>
    <div class="menu">
      <h2 class="menu__title">Our On-The-Run Menu :</h2>
      <ul class="menu__list">
        <li>Organic Coffee, Espresso &amp; Tea</li>
        <li>Blendora Smoothies</li>
        <li>Protein Shakes</li>
        <li>Zesty Pour<span class="menu__note">*100% fresh local fruit and veggies*</span></li>
        <li>Tender Nibs</li>
      </ul>
    </div>
    <p class="contact contact--web"><b>WEBSITE:</b> www.tidy-kettle.com<br><b>EMAIL:</b> Rosalind@tidy-kettle.com</p>
  </section>
</main>
</body>
</html>
```